Aviation: Overcast Study Guide Book Cover

We need a book cover (front and back) designed for an Instrument Flight Rules (IFR) study guide used by helicopter and airplane pilots to obtain an instrument rating for a helicopter or airplane. Below is the title and subtitles.

TITLE: OVERCAST STUDY GUIDE
SUBTITLE 1: Checkride Preparation for Airplane and Helicopter Pilots
SUBTITLE 2: Prepare for your Instrument Rating with Confidence

We have also upload recommended text to be included on the back cover. In addition, we included images of similar book covers that we like and ones that we do not like. Below are links to two others books by the author.

https://www.bookvarro.example/Rotorcraft-Exam-Handbook-oral-review/dp/507214638K
https://www.bookvarro.example/Manual-Floatwing-Handling-Lionel-Quarrick/dp/5093742816

Flight students

Aviation

• helicopter and airplane

```html
<!DOCTYPE html>
<html lang="en">
<head>
<meta charset="utf-8">
<title>Overcast Study Guide – Cover Spread</title>
<link href="https://fonts.googleapis.com/css2?family=Lato:wght@400;700;900&family=Poppins:wght@800&display=swap" rel="stylesheet">
<style>
  :root {
    --page-bg: #111111;
    --cover-blue: #2f86c6;
    --spine-line: #1f5f92;
    --panel-blue: #0a5ba8;
    --accent-yellow: #f8ef5c;
    --ink-dark: #1b1b1b;
    --white: #ffffff;
    --sky-top: #8fb0d2;
    --sky-bottom: #b9cde3;
  }
  * { margin: 0; padding: 0; box-sizing: border-box; }
  html, body { width: 1200px; height: 1200px; overflow: hidden; background: var(--page-bg); }
  .spread {
    position: absolute; left: 87px; top: 275px; width: 1026px; height: 650px;
    background: var(--cover-blue); font-family: "Lato", sans-serif; color: var(--white);
  }
  .back-cover { position: absolute; left: 0; top: 0; width: 503px; height: 650px; }
  .spine {
    position: absolute; left: 503px; top: 0; width: 21px; height: 650px;
    border-left: 1px solid var(--spine-line); border-right: 1px solid var(--spine-line);
  }
  .front-cover { position: absolute; left: 524px; top: 0; width: 502px; height: 650px; }

  .back-heading { position: absolute; left: 43px; width: 416px; text-align: center; font-weight: 400; text-transform: uppercase; }
  .back-heading.main { top: 52px; font-size: 17.5px; line-height: 24px; }
  .back-heading.sub { top: 166px; font-size: 13px; letter-spacing: 0.2px; }
  .back-copy { position: absolute; left: 43px; width: 416px; font-size: 9.4px; line-height: 11.8px; text-align: justify; }
  .back-copy.intro { top: 105px; }
  .back-copy.scope { top: 192px; }
  .back-copy.bio { top: 395px; }
  .bio-name { font-size: 12.5px; font-weight: 700; text-transform: uppercase; }

  .topic-table {
    position: absolute; left: 68px; top: 258px; width: 368px; border-collapse: collapse;
    border: 2px solid var(--white);
  }
  .topic-table td {
    width: 33.33%; height: 24.5px; text-align: center; font-size: 9.5px;
    border: 1.5px solid var(--white);
  }
  .divider { position: absolute; left: 43px; top: 366px; width: 416px; height: 1.5px; background: var(--white); }

  .barcode-panel { position: absolute; left: 356px; top: 565px; width: 118px; height: 71px; background: var(--panel-blue); z-index: 2; }
  .band-yellow { position: absolute; background: var(--accent-yellow); }
  .band-back { left: 0; top: 603px; width: 524px; height: 47px; }

  .title-main {
    position: absolute; left: 0; top: 24px; width: 502px; text-align: center;
    font-family: "Poppins", sans-serif; font-weight: 800; font-size: 86px; line-height: 1;
    letter-spacing: -1px; transform: scaleY(2.05); transform-origin: top center;
  }
  .title-sub {
    position: absolute; left: 0; top: 222px; width: 502px; text-align: center;
    font-family: "Poppins", sans-serif; font-weight: 800; font-size: 52px; line-height: 1;
  }
  .subtitle-band { left: 0; top: 282px; width: 502px; height: 55px; }
  .subtitle-band p {
    text-align: center; color: var(--ink-dark); font-size: 18.5px; line-height: 22px;
    letter-spacing: 1.8px; text-transform: uppercase; padding-top: 6px;
  }
  .cover-photo { position: absolute; left: 0; top: 342px; width: 502px; height: 209px; background: linear-gradient(180deg, var(--sky-top), var(--sky-bottom)); }
  .tagline { position: absolute; left: 0; top: 570px; width: 502px; text-align: center; font-weight: 700; font-size: 16.5px; letter-spacing: 0.4px; }
  .author-band { left: 0; top: 603px; width: 502px; height: 47px; }
  .author-name {
    text-align: center; color: var(--ink-dark); font-weight: 900; font-size: 30px;
    letter-spacing: 5.5px; line-height: 47px; padding-left: 20px;
  }
</style>
</head>
<body>
  <div class="spread">
    <section class="back-cover">
      <h2 class="back-heading main">Prepare for your IFR check ride<br>with confidence</h2>
      <p class="back-copy intro">Becoming an instrument rated pilot is one of the most challenging ratings to obtain. This guide helps prepare you to pass your IFR check ride with confidence. The question-and-answer format is easy to follow and provides detailed explanations for expanded knowledge.</p>
      <h3 class="back-heading sub">Includes helicopter and airplane specific content</h3>
      <p class="back-copy scope">This guide is designed to prepare an airplane or helicopter pilot the oral portion of the IFR checkride. Unlike other resources, this guide specifically addresses the differences with IFR flight in helicopters. As a dual rated pilot, the author ensures to identify areas of differences between the two categories of IFR flight. The following concepts are addressed within the guide</p>
      <table class="topic-table">
        <tr><td>Preflight Actions</td><td>Enroute Procedures</td><td>Aeromedical Factors</td></tr>
        <tr><td>General IFR Concepts</td><td>Approach Procedures</td><td>Weather Fundamentals</td></tr>
        <tr><td>Departure Procedures</td><td>IFR Emergencies</td><td>Risk Management</td></tr>
      </table>
      <div class="divider"></div>
      <p class="back-copy bio"><span class="bio-name">Lionel Quarrick</span> is ATP rated pilot and helicopter and fixed-wing instructor. Lionel is the owner and operator Northwind Ridge, LLC which does business as Crosswind Aviation and Pelican Aviation. Crosswind Aviation provides primary helicopter flight instruction while Pelican Aviation provides seaplane flight instruction and tours. In addition to instructing, Lionel has authored other books to include The Rotorcraft Exam Handbook, and Manual of Floatwing Handling. Lionel lives in Kentucky with his beautiful wife Marla. They have a daughter, Jenna, that is dual rated and employed as a captain for a charter company. Prior to learning to fly, Lionel spent several years in the military as a Special Warfare Combat Craft Crewman in the U.S. Navy and Ranger-qualified infantry officer in the U.S. Army.</p>
      <div class="barcode-panel"></div>
    </section>

    <div class="band-yellow band-back"></div>
    <div class="spine"></div>

    <section class="front-cover">
      <h1 class="title-main">OVERCAST</h1>
      <div class="title-sub">STUDY GUIDE</div>
      <div class="band-yellow subtitle-band"><p>Checkride preparation for<br>airplane and helicopter pilots</p></div>
      <div class="cover-photo" role="img" aria-label="Photo of a dark blue vintage biplane flying against a pale blue sky"></div>
      <p class="tagline">Prepare for your Instrument Rating with Confidence</p>
      <div class="band-yellow author-band"><p class="author-name">LIONEL J. QUARRICK</p></div>
    </section>
  </div>
</body>
</html>
```